Website Refresh for Brightfield Childcare

Company Overview:

Brightfield Childcare is a trusted provider of early childhood education and care services. We are dedicated to creating a nurturing environment where children can grow, learn, and thrive. Our centres offer a range of programs tailored to different age groups, and we pride ourselves on our commitment to quality, safety, and community engagement.

Project Overview:

We are looking for a talented designer to refresh our existing website (https://brightfieldchildcare.com.au/).

The primary goal is to modernize the design while keeping the content unchanged. The new design should be user-friendly, visually appealing, and reflective of our brand’s values. The website should share a similar "DNA" with our sister company’s website, Oak Harbour Early Learning, (https://oakharbourelc.com.au/) but it should not be a direct copy.

We want a design that mirrors our brand's shared values while introducing unique elements that distinguish Brightfield Childcare.

Design Requirements:
1. Home Page
2. About Us
3. Parent Info
4. Our Programs
5. Template for Centre Pages
6. Contact Us / Enrolment (Optional)

Design Style and Inspiration:
• The design should align with the "DNA" of Oak Harbour Early Learning, but also bring in unique design elements to set Brightfield Childcare apart.
• We are looking for a clean, modern, and professional design that is easy to navigate.
• The colour scheme and design elements should reflect our brand’s identity—welcoming, warm, and child-friendly without being overly childish.
• The design must be responsive, ensuring a great user experience across all devices, including desktops, tablets, and mobile phones.
• Accessibility is crucial—use clear fonts, sufficient contrast, and straightforward navigation.

Content Considerations:
• The content will remain the same; the focus is on enhancing the design and user interface.

Deliverables:
• High-fidelity mock-ups for each of the specified pages.
• Responsive design layouts for desktop, tablet, and mobile views.
• Design files should be delivered in a format compatible with any development team.

Target Audience:
• Parents of young children looking for childcare services.
• Community members interested in learning more about our centres and programs.

Submission Requirements:
• A brief explanation of your design approach and how it aligns with our branding goals.
• A portfolio showcasing your previous work, especially any similar projects.
• All requested deliverables must be included in your submission.

Judging Criteria:
• Alignment with our brand identity and the "DNA" of our sister company’s website.
• Visual appeal and user-friendliness of the design.
• Responsiveness and adaptability across different devices.
• Creativity and uniqueness in differentiating Brightfield Childcare from our sister company.

Notes:
• While we would like to engage the winning artist with the coding / css work, its not mandatory.
• Feel free to ask for any digital assets you need to complete the work.
• Main site to be refreshed - https://brightfieldchildcare.com.au/
• Sister site to take inspiration from - https://oakharbourelc.com.au/

Target Market(s)

A) Parents of young children looking for childcare services. B)Community members interested in learning more about our centres and programs.

Industry/Entity Type

Child Care

Number of Pages Required

5+ page

Requirements
Must have
• Please read description
Nice to have
• Please read description
Should not have
• Please read description

```html
<!DOCTYPE html>
<html lang="en">
<head>
<meta charset="utf-8">
<title>Our Programs – Brightfield Childcare</title>
<link href="https://fonts.googleapis.com/css2?family=Poppins:wght@400;600;700;800&family=Open+Sans:wght@400;600&display=swap" rel="stylesheet">
<style>
:root{
  --green:#4f9e2d; --green-dark:#2f6e1b; --green-light:#8cc63f;
  --orange:#f39322; --blue:#1ba1dc; --purple:#8e3a9c; --teal:#17a59a;
  --ink:#333; --muted:#666; --footer:#2b2b2b; --soft:#f6f8f2;
}
*{box-sizing:border-box;margin:0;padding:0}
html,body{width:1200px;height:5316px;overflow:hidden}
body{position:relative;font-family:"Open Sans",sans-serif;color:var(--ink);background:#fff;font-size:14px;line-height:1.6}
h1,h2,h3,h4{font-family:"Poppins",sans-serif}
.abs{position:absolute}
.img{position:absolute;background:linear-gradient(135deg,#8fb86a,#d9b36a 55%,#6c9fc4)}
p{margin-bottom:12px}

/* header */
.topbar{left:0;top:0;width:1200px;height:80px;background:#fff;display:flex;align-items:center;padding:0 40px;gap:30px}
.brand{display:flex;align-items:center;gap:10px;font-family:"Poppins",sans-serif;font-weight:700;font-size:22px;color:var(--green)}
.brand .dot{width:34px;height:34px;border-radius:50%;background:var(--green)}
.contact{margin-left:auto;display:flex;gap:34px;font-size:12px}
.contact div{display:flex;align-items:center;gap:8px}
.contact b{display:block;font-family:"Poppins",sans-serif;font-size:13px}
.contact .ic{width:28px;height:28px;border-radius:50%;background:var(--green);display:flex;align-items:center;justify-content:center;flex:none}
.nav{left:0;top:80px;width:1200px;height:40px;background:var(--green);display:flex;padding-left:40px}
.nav a{color:#fff;text-decoration:none;font-family:"Poppins",sans-serif;font-weight:600;font-size:12px;padding:0 20px;line-height:40px}
.nav a.active{background:var(--orange)}
.hero{left:0;top:120px;width:1200px;height:440px;background:linear-gradient(180deg,#3b4a3a,#5c6b52 60%,#7a8662)}
.hero h1{position:absolute;top:230px;width:100%;text-align:center;color:#fff;font-size:52px;font-weight:800;letter-spacing:1px}
.wave{left:0;width:1200px}

/* intro */
.intro{left:70px;top:600px;width:640px;font-size:13px;color:var(--muted)}
.intro-photo{left:740px;top:620px;width:400px;height:400px;border-radius:50%;border:10px solid #fff;box-shadow:0 0 0 4px var(--green-light)}
.btn{display:inline-block;background:var(--orange);color:#fff;font-family:"Poppins",sans-serif;font-weight:600;font-size:13px;padding:12px 28px;border-radius:4px}
.intro-list{list-style:none;margin-top:10px}
.intro-list li{display:flex;align-items:center;gap:12px;margin-bottom:10px;font-family:"Poppins",sans-serif;font-weight:600;font-size:13px;color:var(--ink)}
.intro-list .bullet{width:26px;height:26px;border-radius:50%;background:var(--teal)}

/* fundamentals */
.fund{left:0;top:1300px;width:1200px;height:480px;background:var(--soft)}
.section-title{font-size:30px;font-weight:700;text-align:center;color:var(--ink)}
.card{position:absolute;top:140px;width:280px;height:200px;background:#fff;border-radius:8px;box-shadow:0 6px 18px rgba(0,0,0,.08);text-align:center;padding-top:30px}
.card .icon{width:80px;height:80px;border-radius:50%;margin:0 auto 26px}
.card h3{font-size:15px;font-weight:700}

/* eylf */
.eylf-title{left:640px;top:1880px;font-size:34px;font-weight:700;line-height:1.25;width:520px}
.eylf-text{left:640px;top:1975px;width:510px;font-size:12.5px;color:var(--muted)}
.pillar{position:absolute;left:640px;display:flex;align-items:center;gap:18px;width:510px;font-family:"Poppins",sans-serif;font-weight:700;font-size:14px}
.pillar .icon{width:50px;height:50px;border-radius:50%;flex:none}
.pillar::after{content:"";position:absolute;left:68px;right:0;bottom:-16px;border-bottom:1px solid #e2e2e2}

/* kindergarten */
.kinder-bg{left:0;top:2680px;width:1200px;height:540px;background:linear-gradient(180deg,#fff,#fdf5ec)}
.kinder-title{left:70px;top:2740px;font-size:32px;font-weight:800;color:var(--orange)}
.kinder-text{left:70px;top:2800px;width:600px;font-size:12.5px;color:var(--muted)}

/* reggio */
.reggio-title{left:560px;top:3310px;font-size:32px;font-weight:800;color:var(--green)}
.reggio-text{left:560px;top:3370px;width:590px;font-size:12.5px;color:var(--muted)}

/* partners */
.partners-title{left:0;top:3900px;width:1200px;font-size:32px;line-height:1.2}
.partner{position:absolute;width:208px;height:250px;background:#fff;border-radius:6px;box-shadow:0 4px 14px rgba(0,0,0,.1);padding:16px;font-size:11px;line-height:1.55;color:var(--muted)}
.partner .mark{display:block;width:56px;height:32px;border-radius:4px;background:#e9eee2;margin-bottom:10px}
.partner h4{font-size:13.5px;font-weight:700;line-height:1.3;color:var(--ink);margin-bottom:3px}
.partner .age{color:var(--orange);font-weight:600;font-family:"Poppins",sans-serif;font-size:11px;display:block;margin-bottom:6px}
.partner .more{position:absolute;bottom:14px;left:16px;font-family:"Poppins",sans-serif;font-weight:700;color:var(--orange);font-size:11px}

/* footer */
.footer{left:0;top:4760px;width:1200px;height:556px;background:var(--footer);color:#ddd}
.footer h4{font-size:15px;color:#fff;margin-bottom:14px}
.footer ul{list-style:none;font-size:13px;line-height:2}
.foot-col{position:absolute;top:120px}
.badge{position:absolute;width:70px;height:70px;border-radius:6px;background:#555}
.foot-bottom{position:absolute;bottom:0;left:0;width:100%;height:46px;background:#1f1f1f;text-align:center;line-height:46px;font-size:12px;color:#aaa}
</style>
</head>
<body>

<header>
  <div class="abs topbar">
    <div class="brand"><span class="dot"></span>Brightfield Childcare</div>
    <div class="contact">
      <div><span class="ic"><svg width="14" height="14" viewBox="0 0 24 24" fill="#fff"><path d="M12 2a7 7 0 0 0-7 7c0 5 7 13 7 13s7-8 7-13a7 7 0 0 0-7-7zm0 9.5A2.5 2.5 0 1 1 12 6a2.5 2.5 0 0 1 0 5.5z"/></svg></span><span><b>ASPLEY</b>12 Sample Road, Aspley QLD</span></div>
      <div><span class="ic"><svg width="14" height="14" viewBox="0 0 24 24" fill="#fff"><path d="M6.6 10.8a15 15 0 0 0 6.6 6.6l2.2-2.2a1 1 0 0 1 1-.25 11.4 11.4 0 0 0 3.6.6 1 1 0 0 1 1 1V20a1 1 0 0 1-1 1A17 17 0 0 1 3 4a1 1 0 0 1 1-1h3.5a1 1 0 0 1 1 1c0 1.25.2 2.45.6 3.6a1 1 0 0 1-.25 1z"/></svg></span><span><b>(07) 3000 0142</b>Call Us Now</span></div>
      <div><span class="ic"><svg width="14" height="14" viewBox="0 0 24 24" fill="#fff"><path d="M3 5h18v14H3zm2 2v.5l7 4.5 7-4.5V7z"/></svg></span><span><b>aspley@brightfieldchildcare.com.au</b>Email Address</span></div>
    </div>
  </div>
  <nav class="abs nav">
    <a href="#">HOME</a><a href="#">ABOUT US</a><a href="#">PARENT INFO</a><a href="#" class="active">OUR PROGRAMS</a><a href="#">TEMPLATE FOR CENTRE</a><a href="#">CONTACT US</a>
  </nav>
  <div class="abs hero" role="img" aria-label="Children playing together in a classroom, darkened behind the page title">
    <h1>OUR PROGRAMS</h1>
  </div>
  <svg class="abs wave" style="top:480px" height="80" viewBox="0 0 1200 80" preserveAspectRatio="none"><path d="M0 40 Q300 0 600 30 T1200 20 V80 H0Z" fill="#fff"/></svg>
</header>

<section>
  <div class="abs intro">
    <p>All programs are planned with a strong emphasis on the fundamentals such as literacy, numeracy, STEAM as well as the creative arts (art, music and dance), development of life skills and problem solving and investigation skills. The weekly programs are influenced by the Early Years Learning Framework with a strong emphasis on Reggio Emilia approach.</p>
    <p>Each program is planned by a qualified Early Childhood Educator. Each child's individual needs and interests are taken into account whilst preparing the room's program. The programs and experiences provided are appropriate to the child's age and stage of development. Children are offered a range of learning experiences both indoors and outdoors.</p>
    <p>Children need to see all that belongs to them and to experience, discover and learn about their world. Our programs take into consideration the multicultural background of the communities they are located in. We aim to break down and challenge traditional stereotypes, respect similarities and differences whilst promoting an atmosphere of inclusiveness. Our educators are respectful of individual differences, interests and styles of learning. We encourage children's independence and aim to increase their awareness of the community and people around them.</p>
    <p>All Brightfield Childcare centres provide opportunities to cultivate deep respect for, and knowledge of, the cultural diversity of the broader community in the educational program, including Aboriginal and Torres Strait Islander histories and cultures.</p>
    <p>At all of our Services we believe in assisting children to develop a deep understanding of being Environmentally Responsible. We foster the children's understanding of the interdependence between people, animals, plants and the land.</p>
    <ul class="intro-list">
      <li><span class="bullet"></span>Early Years Learning Framework (EYLF)</li>
      <li><span class="bullet"></span>Kindergarten Curriculum</li>
      <li><span class="bullet"></span>Reggio Emilia Approach</li>
    </ul>
  </div>
  <div class="img intro-photo" role="img" aria-label="Children exploring a garden outdoors"></div>
  <a class="abs btn" style="left:850px;top:1060px">ENROLMENT INQUIRY</a>
  <svg class="abs wave" style="top:1220px" height="80" viewBox="0 0 1200 80" preserveAspectRatio="none"><path d="M0 80 V50 Q300 10 600 45 T1200 35 V80Z" fill="#f6f8f2"/><path d="M0 80 V62 Q300 30 600 60 T1200 52 V80Z" fill="#8cc63f" opacity=".35"/></svg>
</section>

<section class="abs fund">
  <h2 class="section-title" style="margin-top:70px">ENHASIS ON THE FUNDAMENTALS</h2>
  <div class="card" style="left:120px"><div class="icon" style="background:var(--blue)"></div><h3 style="color:var(--blue)">LANGUAGE &amp; LITERACY</h3></div>
  <div class="card" style="left:460px"><div class="icon" style="background:var(--orange)"></div><h3 style="color:var(--orange)">NUMERACY &amp; MATH</h3></div>
  <div class="card" style="left:800px"><div class="icon" style="background:var(--green)"></div><h3 style="color:var(--green)">ART, MUSIC &amp; DANCE</h3></div>
</section>
<svg class="abs wave" style="top:1700px" height="100" viewBox="0 0 1200 100" preserveAspectRatio="none"><path d="M0 0 H1200 V40 Q900 100 600 60 T0 70Z" fill="#f6f8f2"/><path d="M0 70 Q300 50 600 60 T1200 40 V52 Q900 110 600 72 T0 84Z" fill="#4f9e2d"/></svg>

<section>
  <div class="img" style="left:60px;top:1870px;width:540px;height:480px;border-radius:50% 50% 50% 50%/45% 45% 55% 55%" role="img" aria-label="Collage of children painting and playing in class"></div>
  <h2 class="abs eylf-title">Early Years Learning Framework (EYLF)</h2>
  <div class="abs eylf-text">
    <p>The Early Years Learning Framework describes the principles, practice and outcomes essential to support and enhance young children's learning from birth to five years of age, as well as their transition to school. It also recognises the importance of communication and language, including early literacy and numeracy, and social and emotional development.</p>
    <p>The Framework also has a strong emphasis on play-based learning as play is the best vehicle for young children's learning, providing the most appropriate stimulus for brain development.</p>
  </div>
  <div class="pillar" style="top:2170px"><span class="icon" style="background:var(--blue)"></span>A STRONG SENSE OF IDENTITY</div>
  <div class="pillar" style="top:2250px"><span class="icon" style="background:var(--orange)"></span>CONNECTIONS WITH THEIR WORLD</div>
  <div class="pillar" style="top:2330px"><span class="icon" style="background:var(--green)"></span>STRONG SENSE WELLBEING</div>
  <div class="pillar" style="top:2410px"><span class="icon" style="background:var(--purple)"></span>CONFIDENCE AND INVOLMENT IN THEIR LEARNING</div>
  <div class="pillar" style="top:2490px"><span class="icon" style="background:var(--teal)"></span>EFFECTIVE COMMUNICATION SKILLS</div>
</section>

<section>
  <div class="abs kinder-bg"></div>
  <h2 class="abs kinder-title">KINDERGARTEN CURRICULUM</h2>
  <div class="abs kinder-text">
    <p>Brightfield Childcare centres have Queensland Government funded Kindergarten programs run by fully qualified, registered Kindergarten Teachers across all of our centres.</p>
    <p>The curriculum is based on the Kindergarten Learning Guidelines which are derived from the Early Years Learning Framework for Australia and embrace its inclusive vision that all children experience learning that is engaging and builds success for life.</p>
    <p>While the EYLF focuses on children from birth to five years, the Queensland Kindergarten Guidelines are unique in that they aim to specifically enrich children's learning in the Kindergarten year. In Queensland, the kindergarten year is the year before the preparatory year of schooling. Throughout the Kindergarten year, children's right to experience the joy of childhood is fundamental and learning is promoted through play, and both emergent and planned learning experiences and interactions.</p>
    <p>At Brightfield Childcare we believe that we need to offer the children every opportunity to succeed and therefore in 2011 we introduced our Literacy Program into the Kindergarten curriculum. We have a strong focus on literacy and numeracy skills that engage and challenge the children with many successful outcomes.</p>
  </div>
  <div class="img" style="left:700px;top:2760px;width:460px;height:420px;border-radius:12px" role="img" aria-label="Group of smiling kindergarten children holding a sign"></div>
</section>

<section>
  <div class="img" style="left:40px;top:3300px;width:460px;height:460px;border-radius:50%;border:10px solid #fff;box-shadow:0 0 0 4px var(--green-light)" role="img" aria-label="Child painting at an easel"></div>
  <h2 class="abs reggio-title">REGGIO EMILIA APPROACH</h2>
  <div class="abs reggio-text">
    <p>The Reggio Emilia approach of teaching and learning was founded by the approach's founders in the small town of Reggio Emilia in Italy after world war II. The approach from the start was a movement by the parents of the city to educate their children based on the learning philosophy of the founders, who believed that children from a young age should be taught or encouraged through learning experiences, principles of respect, and becoming responsible citizens of the community.</p>
    <p>In this approach, the learning program is derived from the children's interest; teachers are seen as facilitators of learning. Their role is to plan, prepare and extend children's learning through exploration and discovery in a supportive and enriching environment. We aim to foster in our children: independence, inquisitiveness, persistence and resilience through their daily learning experiences.</p>
    <p>This approach of teaching and learning also places a great emphasis on the appreciation for the arts, fostering creativity and recognising that children are able to express themselves through one hundred languages: this includes drawing, singing, dancing, drama and playing. We believe there is an arts in their expressiveness. This approach correlates dramatically to the traditional chalk and talk, regimented, teacher centred method of teaching and learning.</p>
  </div>
</section>

<section>
  <h2 class="abs section-title partners-title">SOME OF OUR EXTRA CURRICULAR<br>PARTNERS</h2>
  <div class="partner" style="left:40px;top:4060px"><span class="mark"></span><h4>Canvas Kids Art</h4><span class="age">3-5 years</span>Focusing on developing children's creativity, expressing themselves through open-ended art experiences.</div>
  <div class="partner" style="left:268px;top:4060px"><span class="mark"></span><h4>Melody Sprouts Music</h4><span class="age">0-5 years</span>Adapting the ideas of a music teacher to create music programs for early childhood centres.</div>
  <div class="partner" style="left:496px;top:4060px"><span class="mark"></span><h4>Little Linguists</h4><span class="age">3-5 years</span>A complete curriculum based study of friendly languages for appropriate learning experiences.<span class="more">LEARN MORE</span></div>
  <div class="partner" style="left:724px;top:4060px"><span class="mark"></span><h4>Sprint Sprouts Sports</h4><span class="age">3-5 years</span>They offer a fun sports program on a weekly basis, that encourage exploring, nurturing and the environment for little ones to have fun.</div>
  <div class="partner" style="left:952px;top:4060px"><span class="mark"></span><h4>Mini Aces Tennis</h4><span class="age">3-5 years</span>Weekly tennis lessons that teaches the children to begin their physical abilities using industry equipment and fun games.</div>
  <div class="partner" style="left:40px;top:4350px"><span class="mark"></span><h4>Active Tots</h4><span class="age">0-5 years</span>Physical Education programming introducing children to various sports such as soccer, tennis, AFL, rugby, hockey, basketball and many more.</div>
  <div class="partner" style="left:268px;top:4350px"><span class="mark"></span><h4>Brave Hearts Rugby</h4><span class="age">3-5 years</span>A fun and enjoyable set of age appropriate active drills that start on the children's great motor skills while learning the fundamentals of rugby.</div>
  <div class="partner" style="left:496px;top:4350px"><span class="mark"></span><h4>Twirl Dance</h4><span class="age">0-5 years</span>A specialised creative educational movement, music and wellness program for early childhood.</div>
  <div class="partner" style="left:724px;top:4350px"><span class="mark"></span><h4>Dance Classes</h4><span class="age">3-5 years</span>Competent ballet from local centres. They focus on allowing the children to express themselves through different dance genres.</div>
</section>

<svg class="abs wave" style="top:4660px" height="110" viewBox="0 0 1200 110" preserveAspectRatio="none"><path d="M0 110 V60 Q200 20 420 55 T820 40 T1200 50 V110Z" fill="#8cc63f"/><path d="M0 110 V85 Q300 60 600 80 T1200 72 V110Z" fill="#4f9e2d"/></svg>
<footer class="abs footer">
  <div class="brand" style="position:absolute;left:40px;top:60px;color:#fff"><span class="dot"></span>Brightfield Childcare</div>
  <div class="foot-col" style="left:470px"><h4>QUICK LINKS PARENTS</h4><ul><li>Our Programs</li><li>Parent</li><li>Information</li><li>About Us</li><li>Contact</li><li>Our Centres</li></ul></div>
  <div class="foot-col" style="left:780px"><h4>QUICK LINKS EDUCATORS</h4><ul><li>Careers</li><li>Our Centres</li><li>Contact</li><li>About Us</li><li>Our Programs</li></ul></div>
  <div class="badge" style="left:1060px;top:120px"></div>
  <div class="badge" style="left:1060px;top:210px"></div>
  <div class="foot-bottom">© Brightfield Early Learning Centre 2024 | Website Design and Development</div>
</footer>

</body>
</html>
```